KELD, Inc. new buisness cards - brand guide included

We need new business cards. SLEAK SIMPLE FINANCE. They must include a place for NAME, TITLE, CELL, OFFICE PHONE, EMAIL. they also must include our services across the bottom. AIR, OCEAN, FTL, LTL, EXPRESS. for reference this will be being handed to some of the most prestigious shipping companies in a america.

Target Market(s)

Finance and corporate

Contact Information for Business Card

We need new business cards. SLEAK SIMPLE FINANCE. They must include a place for NAME, TITLE, CELL, OFFICE PHONE, EMAIL. they also must include our services across the bottom. AIR, OCEAN, FTL, LTL, EXPRESS.

Requirements
Must have
• We need new business cards. SLEAK SIMPLE FINANCE. They must include a place for NAME, TITLE, CELL, OFFICE PHONE, EMAIL. they also must include our services across the bottom. AIR, OCEAN, FTL, LTL, EXPRESS.
Nice to have
• USE THE COLORS AND LOGO IN THE BRAND GUIDE :)

```html
<!DOCTYPE html>
<html lang="en">
<head>
<meta charset="UTF-8">
<title>KELD, Inc. Business Cards</title>
<link rel="stylesheet" href="https://fonts.googleapis.com/css2?family=Cinzel:wght@500&family=Poppins:wght@400&display=swap">
<style>
  :root {
    --backdrop: #b7b7b7;
    --ink: #333333;
    --paper: #ffffff;
    --shadow: rgba(0, 0, 0, 0.45);
  }
  * { margin: 0; padding: 0; box-sizing: border-box; }
  html, body {
    width: 1200px;
    height: 1200px;
    overflow: hidden;
    background: var(--backdrop);
  }
  .canvas {
    position: relative;
    width: 1200px;
    height: 1200px;
  }
  .card {
    position: absolute;
    top: 303px;
    height: 594px;
    box-shadow: 4px 4px 4px var(--shadow);
    overflow: hidden;
  }
  .card-front {
    left: 200px;
    width: 369px;
    background: var(--ink);
    color: var(--paper);
  }
  .card-back {
    left: 599px;
    width: 364px;
    background: var(--paper);
  }
  .wordmark {
    position: absolute;
    left: 0;
    width: 100%;
    text-align: center;
    font-family: "Cinzel", serif;
    font-weight: 500;
    line-height: 1;
    letter-spacing: 0.04em;
  }
  .card-front .wordmark {
    top: 193px;
    font-size: 86px;
    color: var(--paper);
  }
  .card-back .wordmark {
    top: 131px;
    font-size: 76px;
    color: var(--ink);
  }
  .services {
    position: absolute;
    left: 0;
    top: 516px;
    width: 100%;
    text-align: center;
    font-family: "Poppins", sans-serif;
    font-size: 16px;
    letter-spacing: 0.02em;
    white-space: nowrap;
  }
  .services .sep {
    font-size: 10px;
    vertical-align: 2px;
    margin: 0 7px;
  }
  .contact-panel {
    position: absolute;
    left: 0;
    top: 338px;
    width: 100%;
    height: 256px;
    background: var(--ink);
    color: var(--paper);
    text-align: center;
  }
  .contact-panel::before {
    content: "";
    position: absolute;
    left: 0;
    top: 4px;
    width: 100%;
    height: 2px;
    background: var(--paper);
  }
  .person-name {
    position: absolute;
    top: 52px;
    width: 100%;
    font-family: "Cinzel", serif;
    font-weight: 500;
    font-size: 24px;
    line-height: 1;
  }
  .person-title {
    position: absolute;
    top: 77px;
    width: 100%;
    font-family: "Poppins", sans-serif;
    font-size: 16px;
    line-height: 1;
  }
  .divider {
    position: absolute;
    top: 116px;
    left: 135px;
    width: 93px;
    height: 1px;
    background: var(--paper);
  }
  .contact-line {
    position: absolute;
    width: 100%;
    font-family: "Poppins", sans-serif;
    font-size: 17px;
    line-height: 1;
    letter-spacing: 0.02em;
  }
  .contact-cell { top: 136px; }
  .contact-office { top: 165px; }
  .contact-email { top: 194px; }
</style>
</head>
<body>
<main class="canvas">
  <section class="card card-front">
    <div class="wordmark">KELD</div>
    <p class="services">AIR<span class="sep">○</span>OCEAN<span class="sep">○</span>FTL<span class="sep">○</span>LTL<span class="sep">○</span>EXPRESS</p>
  </section>

  <section class="card card-back">
    <div class="wordmark">KELD</div>
    <div class="contact-panel">
      <h1 class="person-name">DANIEL REEVES</h1>
      <p class="person-title">Managing Director</p>
      <div class="divider"></div>
      <p class="contact-line contact-cell">044-555 210 347</p>
      <p class="contact-line contact-office">044-555 210 348</p>
      <p class="contact-line contact-email">hello@keldmail.com</p>
    </div>
  </section>
</main>
</body>
</html>
```